Buffet Restaurant A0 poster for pavement A Board

We are an 'All you can eat' buffet restaurant in a large competitive shopping mall in the UK. We need a size A0 poster for an 'A board' to stand outside our restaurant on the mall to attract customers. The minimum it has to say is that the price is £9.99. Simple!

Please note: the shop front sign on the photos is not blue, it white led backlit that looks blue on photo. Also logo is very simple text you can see on sign. Also check out tallfernos.net

Target Market(s)

Passers by (see Quaybridge demographic via google search)

Industry/Entity Type

Restaurant

Font styles to use
Sans Serif

Requirements
Must have
• Must do the job of enticing customers to our door

```html
<!DOCTYPE html>
<html lang="en">
<head>
<meta charset="utf-8">
<title>Tall Fernos World Buffet – All You Can Eat £9.99</title>
<link rel="stylesheet" href="https://fonts.googleapis.com/css2?family=Archivo:wght@400;500;600;700;800&display=swap">
<style>
  :root {
    --board: #1e1e1e;
    --board-light: #2f2f2f;
    --chalk: #ecebe6;
    --mustard: #d6b51c;
    --mustard-deep: #6f5c0e;
    --scene-light: #b9b9b6;
    --scene-mid: #8e8e8b;
    --scene-dark: #2a2a2a;
  }
  html, body {
    margin: 0;
    padding: 0;
    width: 848px;
    height: 1200px;
    overflow: hidden;
    background: var(--board);
  }
  .poster {
    position: relative;
    width: 848px;
    height: 1200px;
    overflow: hidden;
    background:
      radial-gradient(ellipse at 96% 22%, rgba(255,255,255,0.16), transparent 18%),
      radial-gradient(ellipse at 4% 28%, rgba(255,255,255,0.10), transparent 16%),
      radial-gradient(ellipse at 50% 45%, var(--board-light), var(--board) 80%);
  }
  .poster svg { display: block; }
  .brand-name {
    font-family: "Archivo", Arial, sans-serif;
    font-weight: 800;
    fill: var(--chalk);
  }
  .brand-tagline {
    font-family: "Archivo", Arial, sans-serif;
    font-weight: 500;
    fill: var(--chalk);
  }
  .rule { stroke: var(--chalk); stroke-width: 4; }
  .offer-word {
    font-family: "Archivo", Arial, sans-serif;
    font-weight: 600;
    fill: var(--mustard);
  }
  .offer-price {
    font-family: "Archivo", Arial, sans-serif;
    font-weight: 500;
    fill: var(--mustard);
  }
  .offer-shadow { fill: var(--mustard-deep); }
  .floor-band { fill: var(--mustard); }
  .chalk-grain { opacity: 0.22; mix-blend-mode: screen; }
</style>
</head>
<body>
<main class="poster">
  <svg width="848" height="1200" viewBox="0 0 848 1200" xmlns="http://www.w3.org/2000/svg">
    <defs>
      <filter id="chalk-noise" x="0" y="0" width="100%" height="100%">
        <feTurbulence type="fractalNoise" baseFrequency="0.9" numOctaves="2" seed="7"/>
        <feColorMatrix type="matrix" values="0 0 0 0 1  0 0 0 0 1  0 0 0 0 1  0 0 0 1.6 -0.9"/>
      </filter>
      <linearGradient id="buffet-scene-fill" x1="0" y1="0" x2="0" y2="1">
        <stop offset="0" stop-color="var(--scene-dark)" stop-opacity="0"/>
        <stop offset="0.25" stop-color="var(--scene-mid)" stop-opacity="0.55"/>
        <stop offset="0.55" stop-color="var(--scene-light)" stop-opacity="0.6"/>
        <stop offset="1" stop-color="var(--scene-mid)" stop-opacity="0.45"/>
      </linearGradient>
    </defs>

    <!-- Chalkboard grain -->
    <rect class="chalk-grain" x="0" y="0" width="848" height="1200" filter="url(#chalk-noise)"/>

    <!-- Header -->
    <line class="rule" x1="44" y1="37" x2="804" y2="37"/>
    <text class="brand-name" x="48" y="171" font-size="143" textLength="752" lengthAdjust="spacingAndGlyphs">TALL FERNOS</text>

    <g class="tagline-row">
      <line class="rule" x1="44" y1="229" x2="193" y2="229"/>
      <text class="brand-tagline" x="424" y="245" font-size="50" text-anchor="middle" textLength="406" lengthAdjust="spacingAndGlyphs">WORLD BUFFET</text>
      <line class="rule" x1="656" y1="229" x2="804" y2="229"/>
    </g>

    <!-- Offer headline -->
    <g class="offer-headline">
      <text class="offer-word" x="16" y="408" font-size="148" textLength="280" lengthAdjust="spacingAndGlyphs">ALL</text>
      <text class="offer-word" x="336" y="349" font-size="72" textLength="157" lengthAdjust="spacingAndGlyphs">YOU</text>
      <text class="offer-word" x="336" y="408" font-size="66" textLength="157" lengthAdjust="spacingAndGlyphs">CAN</text>
      <text class="offer-word" x="541" y="408" font-size="148" textLength="280" lengthAdjust="spacingAndGlyphs">EAT</text>
    </g>

    <g class="offer-only">
      <text class="offer-shadow offer-price" x="313" y="526" font-size="78" textLength="230" lengthAdjust="spacingAndGlyphs">ONLY</text>
      <text class="offer-price" x="309" y="523" font-size="78" textLength="230" lengthAdjust="spacingAndGlyphs">ONLY</text>
    </g>

    <g class="offer-amount">
      <text class="offer-shadow offer-price" x="141" y="736" font-size="230" textLength="587" lengthAdjust="spacingAndGlyphs">£9.99</text>
      <text class="offer-price" x="133" y="731" font-size="230" textLength="587" lengthAdjust="spacingAndGlyphs">£9.99</text>
    </g>

    <!-- Buffet scene -->
    <rect x="27" y="790" width="794" height="341" fill="url(#buffet-scene-fill)" role="img" aria-label="Illustration of three diners serving themselves from a row of steaming buffet dishes"/>
    <rect class="floor-band" x="27" y="1131" width="797" height="24"/>
  </svg>
</main>
</body>
</html>
```